Tallow Crest Business Card

We need a business card designed for a a company called "Tallow Crest". We offer consulting, coaching and training to business leaders and coaches (across the world) using the latest findings in neuroscience, social and emotional intelligence and positive psychology. The final design should communicate the use of brain science to create sustainable relationships.

The card should be doublesided. The logo is attached and names and titles will be provided to the successful designer. Thank you.

Industry/Entity Type

Training

```html
<!DOCTYPE html>
<html lang="en">
<head>
<meta charset="utf-8">
<title>Tallow Crest Business Card</title>
<link rel="stylesheet" href="https://fonts.googleapis.com/css2?family=Open+Sans:wght@400;600;700&display=swap">
<style>
  :root {
    --ocean: #1a8fcf;
    --ocean-deep: #157fbb;
    --lime: #bcd52f;
    --lime-soft: #cde168;
    --white: #ffffff;
    --stage-top: #f2f2f2;
    --stage-bottom: #cfcfcf;
    --card-w: 500px;
    --card-h: 286px;
  }
  * { box-sizing: border-box; margin: 0; padding: 0; }
  html, body { width: 1200px; height: 782px; overflow: hidden; }
  body {
    font-family: "Open Sans", Arial, sans-serif;
    background: radial-gradient(ellipse at 50% 40%, var(--stage-top) 0%, var(--stage-bottom) 100%);
    position: relative;
  }
  .card {
    position: absolute;
    top: 248px;
    width: var(--card-w);
    height: var(--card-h);
    border-radius: 14px;
    overflow: hidden;
    box-shadow: 0 10px 28px rgba(0,0,0,0.18);
    color: var(--white);
  }
  .card--back  { left: 80px;  background: var(--lime); }
  .card--front { left: 620px; background: var(--ocean); }

  .profile-motif {
    position: absolute;
    border-radius: 50%;
  }
  .card--back .profile-motif {
    left: 60px; top: 30px; width: 170px; height: 230px;
    background: radial-gradient(ellipse at center, var(--lime-soft) 0%, rgba(205,225,104,0) 70%);
  }
  .card--front .profile-motif {
    right: -30px; top: 10px; width: 200px; height: 240px;
    background: radial-gradient(ellipse at center, var(--ocean-deep) 0%, rgba(21,127,187,0) 70%);
  }

  .brand {
    position: absolute;
    display: flex;
    flex-direction: column;
    align-items: center;
    gap: 10px;
    font-weight: 700;
    color: var(--white);
    text-align: center;
  }
  .brand__dot {
    width: 58px; height: 58px;
    border-radius: 50%;
    background: var(--white);
  }
  .card--back .brand__dot { opacity: 1; }
  .brand__name { font-size: 26px; letter-spacing: 0.5px; line-height: 1; }
  .card--back .brand { left: 300px; top: 62px; }
  .card--front .brand { left: 0; right: 0; top: 62px; }
  .card--front .brand__name { font-size: 32px; }

  .holder { position: absolute; left: 32px; top: 30px; }
  .holder__name { font-size: 22px; font-weight: 600; line-height: 1.1; }
  .holder__title { font-size: 12px; font-weight: 400; opacity: 0.9; }

  .contact {
    position: absolute; left: 32px; top: 196px;
    font-size: 10px; line-height: 1.45;
  }
  .contact__label { font-weight: 700; margin-right: 4px; }

  .web {
    position: absolute; left: 0; right: 0;
    text-align: center;
    font-size: 11px; font-weight: 600; letter-spacing: 2px;
  }
  .card--back .web { bottom: 5px; }
  .card--front .web { bottom: 20px; }

  .band { position: absolute; left: 0; right: 0; bottom: 0; }
  .card--back .band { height: 24px; background: var(--ocean); }
  .card--front .band { height: 16px; background: var(--lime); }
</style>
</head>
<body>
  <section class="card card--back" aria-label="Card back">
    <div class="profile-motif" role="img" aria-label="Faint head profile decoration"></div>
    <div class="holder">
      <p class="holder__name">Mara Ellison</p>
      <p class="holder__title">Director</p>
    </div>
    <div class="brand">
      <span class="brand__dot"></span>
      <span class="brand__name">Tallow Crest</span>
    </div>
    <div class="contact">
      <p><span class="contact__label">PH:</span>555 010 42 77</p>
      <p><span class="contact__label">MAIL:</span>hello@tallowcrest.com</p>
    </div>
    <div class="band"></div>
    <p class="web">www.tallowcrest.com</p>
  </section>

  <section class="card card--front" aria-label="Card front">
    <div class="profile-motif" role="img" aria-label="Faint head profile decoration"></div>
    <div class="brand">
      <span class="brand__dot"></span>
      <span class="brand__name">Tallow Crest</span>
    </div>
    <p class="web">www.tallowcrest.com</p>
    <div class="band"></div>
  </section>
</body>
</html>
```